4 x Florist Footpath Signage Boards that are consistant with each other for a modern florist

Eye catching, easy to read. little bit floral.
See example attached for wording. We are a modern florist in a country town.
This will be out on the street and needs to stand out!!

The Signage Panels
1. Valentines Day - 14th Feb
2. Workshop Signage boards - see attached example
3. Mothers Day Signage Board - 'Treat mum this Mothers Day'
4. We Are Open

Attached is a copy of the design guidelines and the template. the base of the sign is white.

Target Market(s)

Modern

Industry/Entity Type

Florist

Font styles to use
Sans Serif

Colors
eea4c8
f59296
ffffff
757575

Requirements
Must have
• flowers
• weddings
• giftware
• workshops
• flowers make people happy
• hollybrookblooms.co.nz
Nice to have
• Logo
• little bit of floral or greenery
• my shop is modem and industrial
Should not have
• Needs to be able to read easy

```html
<!DOCTYPE html>
<html lang="en">
<head>
<meta charset="utf-8">
<title>Hollybrook Blooms – Footpath Sign</title>
<link rel="stylesheet" href="https://fonts.googleapis.com/css2?family=Open+Sans:wght@400;700;800&family=Roboto+Condensed:wght@400;700&display=swap">
<style>
  :root {
    --board-pink: #ecc6dc;
    --board-pink-light: #f3d7e6;
    --plank-line: #c9a2b8;
    --blossom-pink: #e66aa0;
    --blossom-white: #f7eef2;
    --leaf-green: #8fb56a;
    --plum: #532a49;
    --plum-soft: #6a3560;
    --ink: #000000;
  }
  * { margin: 0; padding: 0; box-sizing: border-box; }
  html, body { width: 905px; height: 1200px; overflow: hidden; }
  body { position: relative; background: var(--board-pink); font-family: "Open Sans", sans-serif; }

  .board-texture {
    position: absolute; inset: 0;
    background: linear-gradient(180deg, var(--board-pink-light), var(--board-pink));
  }
  .plank-lines { position: absolute; inset: 0; }

  .blossom-spray {
    position: absolute; left: 0; top: 0; width: 905px; height: 900px;
  }

  .headline {
    position: absolute; right: 62px; top: 178px;
    text-align: right; color: var(--plum);
    font-family: "Roboto Condensed", sans-serif; font-weight: 700;
    line-height: 1;
  }
  .headline__flowers { display: block; font-size: 128px; letter-spacing: 1px; transform: scaleX(1.02); transform-origin: right; }
  .headline__make { display: block; font-size: 88px; margin-top: 4px; }
  .headline__happy { display: block; font-size: 152px; margin-top: -6px; margin-right: 42px; }

  .services {
    position: absolute; right: 82px; top: 614px;
    list-style: none; text-align: right; color: var(--plum-soft);
    font-weight: 800; font-size: 34px; letter-spacing: 12px; line-height: 67px;
  }
  .services li { margin-right: -12px; }

  .shop-online {
    position: absolute; left: 152px; top: 990px;
    font-weight: 800; font-size: 48px; letter-spacing: 5px; color: var(--ink);
  }
  .web-address {
    position: absolute; left: 148px; top: 1048px;
    font-family: "Roboto Condensed", sans-serif; font-weight: 400;
    font-size: 46px; letter-spacing: 10px; color: var(--ink);
  }
</style>
</head>
<body>
  <div class="board-texture"></div>
  <svg class="plank-lines" width="905" height="1200" aria-hidden="true">
    <g stroke="var(--plank-line)" stroke-width="3">
      <line x1="130" y1="0" x2="136" y2="1200"/>
      <line x1="330" y1="0" x2="334" y2="1200"/>
      <line x1="540" y1="0" x2="540" y2="1200"/>
      <line x1="762" y1="0" x2="760" y2="1200"/>
    </g>
  </svg>

  <svg class="blossom-spray" role="img" aria-label="Spray of pink and white apple blossom with green leaves along the top and left edge">
    <defs>
      <radialGradient id="blossomTone" cx="30%" cy="20%" r="80%">
        <stop offset="0" stop-color="var(--blossom-white)"/>
        <stop offset="0.5" stop-color="var(--blossom-pink)" stop-opacity="0.85"/>
        <stop offset="1" stop-color="var(--blossom-pink)" stop-opacity="0"/>
      </radialGradient>
    </defs>
    <path d="M0 0 H860 Q840 150 700 170 Q480 200 330 330 Q250 420 260 600 Q250 780 160 880 Q60 900 0 860 Z" fill="url(#blossomTone)"/>
  </svg>

  <h1 class="headline">
    <span class="headline__flowers">FLOWERS</span>
    <span class="headline__make">MAKE PEOPLE</span>
    <span class="headline__happy">HAPPY</span>
  </h1>

  <ul class="services">
    <li>FLOWERS</li>
    <li>WEDDINGS</li>
    <li>GIFTWARE</li>
    <li>WORKSHOPS</li>
  </ul>

  <p class="shop-online">SHOP ONLINE</p>
  <p class="web-address">hollybrookblooms.co.nz</p>
</body>
</html>
```